Wren Motorcar Polishing Flyer Design

Hi, I need a flyer design for the pricing and package display of my business (Wren Motorcar Polishing)

www.kelvora.example/wrenmotorpolish

To keep this short and simple, I will need 2 versions of your finished product, can be similar in design just has to be saying something different.

First flyer will be the general version for all customers.

It will need to include the following!
Format, Placement, Font, Design etc.. is all up to you!

==================================

Package 1 [Cars $49.99][Trucks Vans & SUV's $54.99]: Speed Detail

- Exterior Pressure Clean w/ Spotless water
treatment and Vacuum dried
- Wheel Wells Glossed and Cleaned
- Tires Cleaned and Hand Dried
- Tires Dressed with Gloss Finish
- Exterior and Interior Windows cleaned and Hand Dried
- Interior is Vacuumed and Door jams cleaned to Perfection!

Package 2 [Cars $59.99][Trucks Vans & SUV's $64.99]: Speed Detail & Hand Waxing

- Exterior Pressure Clean w/ Spotless water treatment and Vacuum dried
- Hand Applied Wax Treatment with Delmark's Advanced Spray on wax & Micro Scratch Sealant!

Package 3 [Cars $110.00][Trucks Vans & SUV's $149.99]: Advanced Interior Detail

- Interior & Exterior Windows Cleaned and Hand Dried
- All Vents and Creases cleaned out
- Advanced plastic/vinyl/leather Vellusta Interior Treatment!
- Plastic/Vinyl/Leather Conditioner Vellusta Treatment
- Hand Treated Dust Removal
- Seats/Carpets/Headliner steam cleaned
- Seat Belts/Trunks & Floor Mats Treated and Rejuvenated
- Stain Removal

Package 4 [Cars $110.00][Trucks Vans & SUV's $149.99]: Advanced Exterior Detail

- Exterior Pressure Clean w/ Spotless water treatment and Vacuum dry with additional Hand Drying
- Hand Applied Carnauba Wax & Micro Scratch Sealant Treatment
- Dark Exterior Plastic Restoration Treatment (wherever applicable)

Package 5 [Cars $210][Trucks Vans & SUV's $299.99];The Complete Detail

- Stain Removal

Additional Options (May be applied to existing packages when requested!):

(Clay Bar Treatment): [Cars $69.99][Trucks Vans & SUV's $99.99]

- Removal of all Build-Up on Paint such as Micro debris, stone chips, water spots

(Full Vehicle Polishing): [Cars $75.99][Trucks Vans & SUV's $119.99]

- This process removes marring, swirl marks, scratches, stone chips, water spots and acid etching caused by bird droppings and bug remains.

- Adds a sleek shine when wax is applied after.

(Drop-Q Hand Applied Window Treatment): [Cars $10.00][Trucks Vans & SUV's $15]

- This process repels water, making windshield wipers unneeded during storms and rainy weather.

A percentage of proceeds will be Donated to Help Veterans in need!

Phone #: xxx-xxx-xxxx
Email #: xxxxxxxxxx
Instagram: @
Facebook: kelvora.example/wrenmotorpolish
website: > Coming Soon <

Alright, that will be the first designed flyer.

The next flyer can be single paged or flyer layed out. It is generally aimed towards my first customer Lindqvist Strength and Care. An image of there logo will be provided below along with my logo and current business card so ideas can be drawn beside them.

Wren Motorcar Polishing
The Lindqvist Special (For August)

Package 1 [Cars $24.99][Trucks Vans & SUV's $34.99]: Speed Detail

Package 2 [Cars $39.99][Trucks Vans & SUV's $44.99]: Speed Detail & Hand Waxing

Thanks a TON! If you guy's need anymore information or have any other questions during the design process, please, please; let me know!

Target Market(s)

Automotive Detailing, Mobile Automotive Detailing, Parking Lot Detailing, Business Detailing, etc.

Industry/Entity Type

Automotive

Requirements
Must have
• A Classy Design, I'd like it to match in some form or another the Card pictures I have submitted
Nice to have
• Black and White as primary colors, silver aswell
Should not have
• Not too much Wren orange coloring in the design unless it adds to the overall definition of the finished project. Thanks!

```html
<!DOCTYPE html>
<html lang="en">
<head>
<meta charset="utf-8">
<title>Wren Motorcar Polishing – Lindqvist Special Packages</title>
<link href="https://fonts.googleapis.com/css2?family=Oswald:wght@400;500&family=Raleway:wght@300;400&display=swap" rel="stylesheet">
<style>
  :root {
    --page-bg: #eeeeec;
    --sheet-dark: #23252c;
    --sheet-mid: #30333b;
    --header-grey: #6d6e72;
    --band-grey: #5e5f63;
    --text-white: #ffffff;
    --text-soft: #e6e7ea;
    --accent-red: #e8401f;
    --ring-silver: #d9d9dc;
  }
  * { margin: 0; padding: 0; box-sizing: border-box; }
  html, body { width: 1200px; height: 1000px; overflow: hidden; background: var(--page-bg); }
  .canvas { position: relative; width: 1200px; height: 1000px; }

  .flyer {
    position: absolute; left: 25px; top: 85px; width: 1150px; height: 827px;
    background: radial-gradient(ellipse at 50% 45%, var(--sheet-mid) 0%, var(--sheet-dark) 75%);
  }

  .package-title {
    position: absolute; top: 34px; width: 428px; height: 84px;
    background: var(--header-grey);
    color: var(--text-white);
    font-family: "Raleway", sans-serif; font-weight: 300;
    font-size: 46px; letter-spacing: 1px;
    line-height: 84px; padding-left: 22px;
  }
  .package-title--one { left: 52px; }
  .package-title--two { left: 675px; }

  .vehicle-label {
    position: absolute; color: var(--text-white);
    font-family: "Oswald", sans-serif; font-weight: 400;
    font-size: 30px; line-height: 35px;
  }

  .price-badge {
    position: absolute; width: 98px; height: 98px;
    border-radius: 50% 14% 50% 50%;
    background: linear-gradient(135deg, #ffffff 0%, var(--ring-silver) 50%, #8b8c90 100%);
    box-shadow: 0 3px 6px rgba(0,0,0,.5);
  }
  .price-badge span {
    position: absolute; inset: 6px;
    border-radius: 50% 14% 50% 50%;
    background: var(--accent-red);
    display: flex; align-items: center; justify-content: center;
    color: var(--text-white);
    font-family: "Oswald", sans-serif; font-weight: 500; font-size: 25px;
  }

  .divider {
    position: absolute; left: 577px; top: 130px; width: 2px; height: 345px;
    background: linear-gradient(to bottom, transparent, #9a9ca3 50%, transparent);
  }

  .service-list {
    position: absolute; top: 274px; list-style: none;
    color: var(--text-soft);
    font-family: "Raleway", sans-serif; font-weight: 400; font-size: 17px; line-height: 17px;
  }
  .service-list--one { left: 77px; width: 440px; }
  .service-list--two { left: 671px; width: 440px; }
  .service-list li { position: relative; padding-left: 20px; margin-bottom: 11px; }
  .service-list li::before {
    content: ""; position: absolute; left: 2px; top: 2px;
    width: 14px; height: 14px; border-radius: 50% 20% 50% 50%;
    background: var(--accent-red);
  }

  .photo-strip {
    position: absolute; left: 45px; top: 545px; width: 1058px; height: 167px;
    display: flex; gap: 1px;
  }
  .photo { height: 100%; }
  .photo--cabin { width: 200px; background: linear-gradient(160deg, #5a5b5f, #1e1f22); }
  .photo--engine { width: 186px; background: linear-gradient(170deg, #3a3b3e, #b8b9bb 55%, #6b6c70); }
  .photo--trunk { width: 222px; background: linear-gradient(180deg, #2a2a2c 0%, #3b3b3d 45%, #e8381a 60%, #c92a12 100%); }
  .photo--exhaust { width: 222px; background: linear-gradient(160deg, #8c1c1a 0%, #d4d4d6 40%, #a77b5d 100%); }
  .photo--seats { width: 224px; background: linear-gradient(160deg, #8e8f92, #c9c9cb 55%, #9fa0a3); }

  .donation-band {
    position: absolute; left: 45px; top: 712px; width: 1058px; height: 51px;
    background: var(--band-grey);
    color: var(--text-white);
    font-family: "Raleway", sans-serif; font-weight: 400; font-size: 20px; letter-spacing: .6px;
    text-align: center; line-height: 51px;
  }
</style>
</head>
<body>
<div class="canvas">
  <section class="flyer">
    <h2 class="package-title package-title--one">PACKAGE 1</h2>
    <h2 class="package-title package-title--two">PACKAGE 2</h2>

    <div class="vehicle-label" style="left:55px;top:143px;">CARS</div>
    <div class="price-badge" style="left:129px;top:137px;"><span>$24.99</span></div>
    <div class="vehicle-label" style="left:280px;top:138px;">TRUCKS<br>VANS &amp;<br>SUV's</div>
    <div class="price-badge" style="left:384px;top:137px;"><span>$34.99</span></div>

    <div class="vehicle-label" style="left:675px;top:143px;">CARS</div>
    <div class="price-badge" style="left:747px;top:137px;"><span>$39.99</span></div>
    <div class="vehicle-label" style="left:905px;top:138px;">TRUCKS<br>VANS &amp;<br>SUV's</div>
    <div class="price-badge" style="left:1009px;top:137px;"><span>$44.99</span></div>

    <div class="divider"></div>

    <ul class="service-list service-list--one">
      <li>Exterior Pressure Clean w/ Spotless water treatment and Vacuum dried</li>
      <li>Wheel Wells Glossed and Cleaned</li>
      <li>Tires Cleaned and Hand Dried</li>
      <li>Tires Dressed with Gloss Finish</li>
      <li>Exterior and Interior Windows cleaned and Hand Dried</li>
      <li>Interior is Vacuumed and Door jams cleaned to Perfection!</li>
    </ul>

    <ul class="service-list service-list--two">
      <li>Exterior Pressure Clean w/ Spotless water treatment and Vacuum dried</li>
      <li>Wheel Wells Glossed and Cleaned</li>
      <li>Tires Cleaned and Hand Dried</li>
      <li>Tires Dressed with Gloss Finish</li>
      <li>Exterior and Interior Windows cleaned and Hand Dried</li>
      <li>Interior is Vacuumed and Door jams cleaned to Perfection!</li>
      <li>Hand Applied Wax Treatment with Delmark's Advanced Spray on wax &amp; Micro Scratch Sealant!</li>
    </ul>

    <div class="photo-strip">
      <div class="photo photo--cabin" role="img" aria-label="Photo of a detailed car cabin with clean front seats and console"></div>
      <div class="photo photo--engine" role="img" aria-label="Photo of a cleaned V6 engine bay"></div>
      <div class="photo photo--trunk" role="img" aria-label="Photo of the clean open trunk of a red hatchback"></div>
      <div class="photo photo--exhaust" role="img" aria-label="Photo of polished twin exhaust tips under a red tail light"></div>
      <div class="photo photo--seats" role="img" aria-label="Photo of clean grey leather seats inside a van"></div>
    </div>

    <div class="donation-band">A PERCENTAGE OF PROCEEDS WILL BE DONATED TO HELP VETERANS IN NEED!</div>
  </section>
</div>
</body>
</html>
```